Fernvale Pantry web design

Go to fernvalepantry.com.au an using the current layout create a design that will attract customers to this wholefood website.

You may suggest / make slight changes to the layout to create effective graphic design principles.

The LOGO design is TM already. So no changes there. Second logo attached is authorised for use and is a area branding LOGO.

Colours need to reflect health and wellbeing.

Don't want Medical style or New age.
Updates

Logo now loaded

Thank you for your submissions so far. I have sent them out to a trusty panel of friends to hear what they have to say. Some of you have done very well.

Project Deadline Extended
Reason: There are a few submissions outstanding. I will eliminate a few designs today and give feed back. Thankyou

Thank you for your submissions so far I will not be asking for more design submissions from other designers. The ones I have are under consideration and there are a few minor changes to each that may just bring out the one that is IT! The two designs I have narrowed it down to are very different in approach so please bear with me a couple more days. Thank you.

Target Market(s)

Whole food health concious people target market locally Home Delivery would be young Mums with restricted movement because of young children. Older people that are restricted transport users.

Busy commuters that leave our area for work and just want to relax on the weekend with their family and local bush walking or garden activities.

Industry/Entity Type

Graphic Design

Requirements
Should not have
• Medical or sterile hospital feel. New age or too alternative living feel.

```html
<!DOCTYPE html>
<html lang="en">
<head>
<meta charset="utf-8">
<title>Fernvale Pantry</title>
<link rel="stylesheet" href="https://fonts.googleapis.com/css2?family=Open+Sans:ital,wght@0,400;0,600;0,700;0,800;1,700;1,800&display=swap">
<style>
:root{
  --purple:#63165e;
  --green:#8dc63f;
  --green-dark:#6aa22a;
  --ink:#222;
  --grey:#8a8a8a;
  --line:#dedede;
  --red:#d81e1e;
  --blue:#2b6cb3;
  --dark:#3b3b3b;
  --white:#fff;
}
*{box-sizing:border-box;margin:0;padding:0}
html,body{width:1200px;height:2734px;overflow:hidden}
body{font-family:"Open Sans",Arial,sans-serif;color:var(--ink);background:var(--white);font-size:13px}
.wrap{width:1030px;margin:0 auto;position:relative}
ul{list-style:none}

.topbar{height:27px;background:var(--purple);color:var(--white);font-size:11px}
.topbar .wrap{display:flex;justify-content:space-between;align-items:center;height:27px}
.topbar .contact{display:flex;gap:22px}

.header{height:101px;position:relative}
.nav-band{position:absolute;top:28px;left:0;right:0;height:60px;background:var(--green)}
.nav{height:60px;display:flex;align-items:center;font-size:14px;font-weight:600;color:var(--white);text-transform:uppercase}
.nav a{display:block;padding:0 22px;line-height:60px}
.nav a.active{background:var(--green-dark)}
.nav .gap{width:250px}
.search{margin-left:auto;width:210px;height:26px;background:var(--white);border:1px solid #cfcfcf}
.logo{position:absolute;left:50%;top:-2px;transform:translateX(-50%);width:200px;height:100px;background:var(--white);border-radius:50px;display:flex;align-items:center;justify-content:center;gap:8px;box-shadow:0 2px 4px rgba(0,0,0,.12)}
.logo .dot{width:16px;height:16px;border-radius:50%;background:var(--green)}
.logo span{font-weight:800;font-size:19px;color:var(--purple)}

.hero{height:434px;position:relative;background:linear-gradient(100deg,#eef5fb 0%,#cfe3f2 40%,#a9cfe6 62%,#9cc27a 85%,#7da845 100%)}
.hero-copy{position:absolute;left:228px;top:70px;width:330px}
.hero-copy h1{font-style:italic;font-weight:800;font-size:44px;line-height:52px;color:#1f5e8a}
.hero-copy p{margin-top:14px;font-size:14px;font-weight:600;color:#2e4b5e;line-height:20px}
.btn{display:inline-block;background:var(--green);color:var(--white);font-weight:700;border-radius:3px}
.hero-copy .btn{margin-top:24px;padding:10px 30px;font-size:14px}
.arrow{position:absolute;top:200px;width:30px;height:30px}
.arrow.left{left:10px}.arrow.right{right:10px}

.login{height:70px;background:var(--purple)}
.login .wrap{display:flex;align-items:center;height:70px;gap:22px;color:var(--white);font-size:13px}
.field{width:230px;height:34px;background:var(--white);color:#aaa;padding:7px 12px;font-size:12px}
.remember{display:flex;align-items:center;gap:8px}
.remember i{width:16px;height:16px;background:var(--white);display:block}
.login .btn{width:150px;text-align:center;line-height:34px;font-size:13px;border-radius:0}

.deals{height:371px}
.section-title{font-size:24px;font-weight:800;padding-top:12px}
.products{display:flex;justify-content:space-between;margin-top:16px}
.product{width:200px;text-align:center}
.product .img{height:180px}
.product h3{font-size:12.5px;font-weight:800;margin-top:12px;line-height:16px}
.price{color:var(--red);font-weight:700;font-size:13px}
.product p{color:var(--grey);font-size:11px;line-height:14px;margin-top:4px}
.product .btn{margin-top:6px;padding:3px 14px;font-size:11px}

.main{height:911px}
.main .wrap{display:flex;justify-content:space-between}
.sidebar{width:295px}
.side-head{height:37px;background:var(--green);color:var(--white);font-size:15px;font-weight:600;padding:7px 10px}
.side-list li{height:23px;border-bottom:1px solid var(--line);color:var(--grey);font-size:11.5px;padding:3px 6px}
.side-list li.first{color:var(--ink)}
.side-head.second{margin-top:34px}
.content{width:723px}
.news-head{height:37px;background:var(--green);color:var(--white);font-size:21px;font-weight:800;padding:3px 12px}
.news{display:flex;justify-content:space-between;height:115px;margin-top:10px}
.news .text{width:560px}
.news h4{font-size:15px;font-weight:600}
.news p{color:var(--grey);font-size:12.5px;line-height:18px;margin-top:4px}
.news .more{color:var(--green-dark);font-size:12.5px;font-weight:600}
.news .thumb{width:120px;height:90px}
.quote{margin-top:44px;height:228px;background:var(--dark);display:flex}
.quote .photo{width:240px;background:linear-gradient(180deg,#f4f4f4,#dcdcdc)}
.quote .body{flex:1;position:relative;color:var(--white);padding:30px 50px 0 60px;font-size:14.5px;line-height:24px}
.qm{position:absolute;font-size:70px;font-weight:800;line-height:1;color:#cfcfcf}
.qm.open{left:14px;top:6px}.qm.close{right:16px;bottom:-20px}

.payments{height:146px;display:flex;align-items:center}
.payments .wrap{border-top:1px solid var(--line);border-bottom:1px solid var(--line);height:90px;display:flex;justify-content:space-between;align-items:center;padding:0 30px}
.pay{width:130px;height:60px;border:1px solid var(--line);border-radius:4px;display:flex;align-items:center;justify-content:center;font-weight:800;font-size:18px;color:var(--blue)}

.footer{height:340px;background:var(--green);color:var(--white)}
.footer .wrap{display:flex;padding-top:40px}
.fcol h5{font-size:19px;font-weight:600;padding-bottom:6px;border-bottom:1px solid rgba(255,255,255,.6);margin-bottom:14px}
.fcol li{font-size:11.5px;line-height:21px;font-weight:600}
.fcol.c1{width:280px}.fcol.c2{width:240px}.fcol.c3{width:170px}
.newsletter{width:330px;height:220px;background:var(--blue);padding:18px 30px;margin-left:10px}
.newsletter h5{font-size:20px;font-weight:600;border-bottom:1px solid rgba(255,255,255,.6);padding-bottom:6px;margin-bottom:16px}
.newsletter .field{width:100%;margin-bottom:12px;height:30px;padding:6px 10px}
.newsletter .btn{padding:6px 26px;font-size:13px}

.partner{height:304px;text-align:center}
.partner-mark{padding-top:45px;display:flex;justify-content:center;align-items:center;gap:14px}
.partner-mark i{display:block;width:30px;height:30px;border-radius:50%;background:#2f7fc1}
.partner-mark span{font-size:28px;font-weight:800;color:#1f4f8f;line-height:34px}
.links{margin-top:60px;font-size:15px;font-weight:700}
.social{margin-top:30px;display:flex;justify-content:center;gap:14px}
.social span{width:62px;height:62px;border-radius:50%;display:flex;align-items:center;justify-content:center;color:var(--white);font-size:13px;font-weight:700}
.s1{background:#3b5998}.s2{background:#dd4b39}.s3{background:#33a7e0}.s4{background:#d9332b}

.bottombar{height:30px;background:var(--purple);color:var(--white);font-size:11px}
.bottombar .wrap{display:flex;justify-content:space-between;align-items:center;height:30px}
.minisocial{display:flex;gap:6px}
.minisocial i{width:16px;height:16px;border-radius:50%;background:var(--white);display:block}
</style>
</head>
<body>

<div class="topbar"><div class="wrap">
  <span>My account | Shopping cart | Checkout | Login</span>
  <span class="contact"><span>(02) 4700 1234</span><span>hello@fernvalepantry.com.au</span></span>
</div></div>

<header class="header">
  <div class="nav-band">
    <nav class="wrap nav">
      <a class="active">Home</a><a>Shop</a><a>Purchase by weight</a>
      <span class="gap"></span>
      <a>Recipes</a><a>Blogs</a>
      <span class="search"></span>
    </nav>
  </div>
  <div class="logo"><i class="dot"></i><span>Fernvale Pantry</span></div>
</header>

<section class="hero" role="img" aria-label="Photo of a smiling family walking through a sunny green meadow">
  <svg class="arrow left" viewBox="0 0 30 30"><circle cx="15" cy="15" r="14" fill="#fff" stroke="#999"/><path d="M18 8l-7 7 7 7" fill="none" stroke="#555" stroke-width="2.5"/></svg>
  <div class="hero-copy">
    <h1>We Create<br>Healthy Food</h1>
    <p>Lorem Ipsum is simply dummy text of the printing and typesetting industry.</p>
    <span class="btn">Read More</span>
  </div>
  <svg class="arrow right" viewBox="0 0 30 30"><circle cx="15" cy="15" r="14" fill="#fff" stroke="#999"/><path d="M12 8l7 7-7 7" fill="none" stroke="#555" stroke-width="2.5"/></svg>
</section>

<section class="login"><div class="wrap">
  <span class="field">Username</span>
  <span class="field">Password</span>
  <span class="remember"><i></i>Remember me</span>
  <span class="btn">REGISTER</span>
  <span>Forget Your Password?</span>
</div></section>

<section class="deals"><div class="wrap">
  <h2 class="section-title">LATEST DEALS</h2>
  <div class="products">
    <div class="product">
      <div class="img" role="img" aria-label="Jar of fresh ground peanut butter" style="background:linear-gradient(160deg,#e0a567,#b06a2f)"></div>
      <h3>FRESH GROUND<br>PEANUT BUTTER 200G</h3>
      <div class="price">Now: $3.39</div>
      <p>This nut butter has been lovingly made with no additives.</p>
      <span class="btn">Add To Cart</span>
    </div>
    <div class="product">
      <div class="img" role="img" aria-label="Bottles of probiotic capsules" style="background:linear-gradient(180deg,#fff,#e7edf4 60%,#2d5aa6)"></div>
      <h3>GUT BALANCE<br>PLUS 30C</h3>
      <div class="price">Now: $21.95</div>
      <p>25 billion good bacteria per capsule. RRP 29.95</p>
      <span class="btn">Add To Cart</span>
    </div>
    <div class="product">
      <div class="img" role="img" aria-label="Bowl of ground linseed, sunflower and almond meal" style="background:radial-gradient(circle,#9c8262 45%,#6a5744 70%,#fff 71%)"></div>
      <h3>LSA</h3>
      <div class="price">Now: $1.60</div>
      <p>This is a high protein meal.<br>Keep refrigerated.</p>
      <span class="btn">Add To Cart</span>
    </div>
    <div class="product">
      <div class="img" role="img" aria-label="Jar of fresh ground peanut butter" style="background:linear-gradient(160deg,#e0a567,#b06a2f)"></div>
      <h3>FRESH GROUND<br>PEANUT BUTTER 200G</h3>
      <div class="price">Now: $3.39</div>
      <p>This nut butter has been lovingly made with no additives.</p>
      <span class="btn">Add To Cart</span>
    </div>
  </div>
</div></section>

<section class="main"><div class="wrap">
  <aside class="sidebar">
    <div class="side-head">Product Categories</div>
    <ul class="side-list">
      <li class="first">Alternative goods</li><li>Dairy Free</li><li>Gluten Free</li><li>Grocery</li><li>Health Supplements</li><li>Natural Grocer</li><li>Organic</li><li>Recipes</li><li>Seasonal</li><li>Specials</li><li>Sugar Replacements</li><li>Vegan</li><li>Vegetarian</li>
    </ul>
    <div class="side-head second">By Weight Categories</div>
    <ul class="side-list">
      <li class="first">Baking</li><li>Beans &amp; Peas</li><li>Candy &amp; Sweet Foods</li><li>Cereals &amp; Flakes</li><li>Coffee &amp; Tea</li><li>Dried Fruit</li><li>Flour</li><li>Free Range Meat</li><li>Gluten Free Produced Meal</li><li>Grains</li><li>Honey Sugar &amp; Natural Replacements</li><li>Muesli</li><li>Nuts</li><li>Pasta</li><li>Pasture Fed Beef</li><li>Pasture Fed Lamb</li><li>Pets</li><li>Preservative Free Meat</li><li>Seeds</li><li>Snacks</li><li>Specials</li>
    </ul>
  </aside>

  <div class="content">
    <div class="news-head">LATEST NEWS</div>
    <article class="news"><div class="text">
      <h4>History of the almond.</h4>
      <p>In history the almond tree has always been a favourite, and in old English times, as the herbal writers tell us, almond trees grew in our gardens and orchards.</p>
      <span class="more">Read More</span></div>
      <div class="thumb" role="img" aria-label="Whole almonds" style="background:linear-gradient(150deg,#fff,#c89a6a 60%,#8a5a34)"></div></article>
    <article class="news"><div class="text">
      <h4>Bliss Balls with Linseed Meal</h4>
      <p>Lorem Ipsum is simply dummy text of the printing and typesetting industry. Lorem Ipsum has been the industry's standard dummy text ever since the 1500s.</p>
      <span class="more">Read More</span></div>
      <div class="thumb" role="img" aria-label="Plate of bliss balls" style="background:linear-gradient(150deg,#d9c7aa,#7b5b3e)"></div></article>
    <article class="news"><div class="text">
      <h4>Home Deliveries</h4>
      <p>$10 Flat Rate - Thursdays 12 - 5 Fernvale to Ridgeview Fridays 9 - 12 Fernvale to Stonebridge</p>
      <span class="more">Read More</span></div>
      <div class="thumb" role="img" aria-label="Delivery box of groceries" style="background:linear-gradient(150deg,#cfcfcf,#6f6f6f)"></div></article>
    <article class="news"><div class="text">
      <h4>Courses</h4>
      <p>Information session on Growing Healthy Cultures and Fermented Foods TBA click 4 more info</p>
      <span class="more">Read More</span></div>
      <div class="thumb" role="img" aria-label="Bowl of fermented grains" style="background:linear-gradient(150deg,#f7f2e2,#d8cfa8)"></div></article>
    <article class="news"><div class="text">
      <h4>Courses</h4>
      <p>Information session on Growing Healthy Cultures and Fermented Foods TBA click 4 more info</p>
      <span class="more">Read More</span></div>
      <div class="thumb" role="img" aria-label="Bowl of fermented grains" style="background:linear-gradient(150deg,#f7f2e2,#d8cfa8)"></div></article>

    <div class="quote">
      <div class="photo" role="img" aria-label="Portrait of a smiling customer in a dark jacket"></div>
      <div class="body">
        <span class="qm open">&ldquo;</span>
        Lorem Ipsum is simply dummy text of the printing and typesetting industry. Lorem Ipsum has been the industry's standard dummy text ever since the 1500s, when an unknown printer took a galley of type and scrambled it to make a type specimen book. It has survived not only five centuries, but also the leap into electronic typesetting,
        <span class="qm close">&rdquo;</span>
      </div>
    </div>
  </div>
</div></section>

<section class="payments"><div class="wrap">
  <span class="pay">Cardwell</span><span class="pay">Velora</span><span class="pay">Tilepay</span><span class="pay">Findara</span><span class="pay">Amberline</span><span class="pay">Paxo</span>
</div></section>

<footer class="footer"><div class="wrap">
  <div class="fcol c1"><h5>Latest Content</h5><ul>
    <li>Fresh Ground Peanut Butter 700g</li><li>Fresh Ground Peanut Butter 400g</li><li>Fresh Ground Peanut Butter 200g</li><li>Bliss Balls with Linseed Meal</li><li>History of the almond</li><li>Greenleaf Organic Tamari 250ml</li><li>Meadow Organic Unhulled Tahini</li><li>Meadow Organic Hulled Tahini</li><li>Wattlecreek Organic Labna</li><li>Wattlecreek Organic Marinated Feta in Oil</li>
  </ul></div>
  <div class="fcol c2"><h5>About Us</h5><ul>
    <li>Special Orders</li><li>Newsletter</li><li>Welcome to Fernvale</li><li>Fernvale Pantry</li><li>Contact Us</li>
  </ul></div>
  <div class="fcol c3"><h5>Help</h5><ul>
    <li>Privacy</li><li>Product Recall</li><li>Legals</li><li>Customer Agreement</li>
  </ul></div>
  <div class="newsletter"><h5>Newsletter</h5>
    <span class="field" style="display:block">Username</span>
    <span class="field" style="display:block">Password</span>
    <span class="btn">Submit</span>
  </div>
</div></footer>

<section class="partner">
  <div class="partner-mark"><i></i><span>Ridgeline<br>Sustainable Business</span></div>
  <div class="links">Home / About Us / Privacy Policy / Site-map / Contact Us</div>
  <div class="social"><span class="s1">Kinra</span><span class="s2">Plexo</span><span class="s3">Flit</span><span class="s4">Clipz</span></div>
</section>

<div class="bottombar"><div class="wrap">
  <span>copyright ©2014</span>
  <span class="minisocial"><i></i><i></i><i></i><i></i><i></i></span>
</div></div>

</body>
</html>
```